Modern, Clean, Edgy & Fun Comedy Show Flyer

We need to a create a new flyer for the comedy show, Harbor Laugh Nights. The original version of the flyer is attached (file: Old flyer), as well as two versions of the logo.
- The text should be the same except now the show is Every First Wednesday and the next show is June 1.
- Remove the jerk shop logo
- Remove the picture of the man, and replace it with a photo of Dale (our host), the Audience, or something of your own design.
* pictures of Dale and the Audience is attached.
* We'd like to keep the same color palette and have also attached a color palette for reference

I have also attached 4 references of flyers that I like, that you can use to get an idea of the theme and aesthetic we are looking for.
* Files: Reference 1, Reference 2, Reference 3, Reference 4
Updates

Colors
3277b5
85acd3
0455a3
eaf1f7
cee9f5
ecf7fb
d5d5d5
e6e6e6

Requirements
Must have
• The harbor laugh nights logo attached
• The text as specified in the project description
• An option with Dale and without

```html
<!DOCTYPE html>
<html lang="en">
<head>
<meta charset="utf-8">
<title>Harbor Laugh Nights – Comedy Show Flyer</title>
<link href="https://fonts.googleapis.com/css2?family=Anton&family=Saira+Condensed:ital,wght@1,800&display=swap" rel="stylesheet">
<style>
  :root {
    --blue-deep: #0455a3;
    --blue-mid: #3277b5;
    --blue-light: #85acd3;
    --ice: #eaf1f7;
    --navy: #060d1c;
    --ink: #111111;
    --white: #ffffff;
  }
  html, body {
    margin: 0;
    padding: 0;
    width: 1200px;
    height: 1200px;
    overflow: hidden;
    background: var(--white);
  }
  .canvas {
    position: relative;
    width: 1200px;
    height: 1200px;
    background: var(--white);
  }
  .flyer {
    position: absolute;
    left: 94px;
    top: 205px;
    width: 1012px;
    height: 783px;
    overflow: hidden;
    font-family: "Saira Condensed", "Arial Narrow", sans-serif;
  }
  .flyer__photo {
    position: absolute;
    inset: 0;
    background:
      radial-gradient(ellipse 420px 260px at 78% 4%, rgba(255,255,255,0.95), rgba(234,241,247,0.55) 45%, rgba(234,241,247,0) 75%),
      radial-gradient(circle 60px at 17% 16%, rgba(220,240,255,0.9), rgba(220,240,255,0) 100%),
      linear-gradient(to top, var(--blue-deep) 0%, rgba(4,85,163,0.7) 18%, rgba(4,85,163,0) 42%),
      linear-gradient(110deg, #0b2230 0%, #12303f 35%, #1c2f55 60%, #0a1530 100%);
  }
  .flyer__photo::after {
    content: "";
    position: absolute;
    inset: 0;
    background: linear-gradient(to left, rgba(4,8,20,0.85) 0%, rgba(4,8,20,0) 45%);
    mask: linear-gradient(to top, #000 0%, #000 45%, transparent 75%);
  }
  .show-logo {
    position: absolute;
    left: 616px;
    top: 68px;
    margin: 0;
    font-family: "Anton", "Impact", sans-serif;
    font-weight: 400;
    font-size: 62px;
    line-height: 1.02;
    color: var(--ink);
    text-transform: uppercase;
  }
  .headline {
    position: absolute;
    left: 238px;
    top: 480px;
    margin: 0;
    font-family: "Anton", "Impact", sans-serif;
    font-weight: 400;
    font-size: 86px;
    line-height: 1;
    color: var(--white);
    text-transform: uppercase;
    white-space: nowrap;
    transform: scaleX(0.92);
    transform-origin: left top;
  }
  .schedule {
    position: absolute;
    left: 238px;
    top: 576px;
    margin: 0;
    font-family: "Anton", "Impact", sans-serif;
    font-size: 58px;
    line-height: 1;
    color: var(--blue-light);
    text-transform: uppercase;
    white-space: nowrap;
    transform: scaleX(0.92);
    transform-origin: left top;
  }
  .schedule sup { font-size: 24px; vertical-align: 24px; margin-right: 4px; }
  .host-line {
    position: absolute;
    left: 58px;
    top: 656px;
    margin: 0;
    font-size: 34px;
    line-height: 1;
    text-transform: uppercase;
    font-style: italic;
    font-weight: 800;
    color: var(--blue-light);
    white-space: nowrap;
  }
  .host-line .host-line__date { color: var(--white); }
  .venue-line {
    position: absolute;
    left: 56px;
    top: 711px;
    margin: 0;
    font-size: 30px;
    letter-spacing: 1.3px;
    line-height: 1;
    font-style: italic;
    font-weight: 800;
    color: var(--white);
    text-transform: uppercase;
    white-space: nowrap;
  }
  .lineup {
    position: absolute;
    left: 698px;
    top: 490px;
  }
  .lineup__label {
    margin: 0 0 16px;
    font-size: 32px;
    font-style: italic;
    font-weight: 800;
    color: var(--blue-light);
    text-transform: lowercase;
    line-height: 1;
  }
  .lineup__list {
    list-style: none;
    margin: 0;
    padding: 0 0 0 4px;
    font-size: 32px;
    font-style: italic;
    font-weight: 800;
    line-height: 30px;
    text-transform: lowercase;
    white-space: nowrap;
  }
  .lineup__list li { color: var(--white); }
  .lineup__list li:nth-child(even) { color: var(--ice); opacity: 0.85; }
</style>
</head>
<body>
<div class="canvas">
  <section class="flyer">
    <div class="flyer__photo" role="img" aria-label="Blue-toned photo of a comedian on stage with a microphone in front of a seated audience in a brick-walled club"></div>

    <h2 class="show-logo">Harbor Laugh<br>Nights</h2>

    <h1 class="headline">Comedy Show</h1>
    <p class="schedule">Every 1<sup>st</sup>Wednesday</p>
    <p class="host-line">Hosted by Dale Marlowe <span class="host-line__date">Wednesday June 1st</span></p>
    <p class="venue-line">The Ink Crate, 42 Pier Lane, Brooklyn, admission free | doors 6.30pm</p>

    <div class="lineup">
      <p class="lineup__label">featuring</p>
      <ul class="lineup__list">
        <li>Wesley Hartline</li>
        <li>Corey Vance</li>
        <li>Eli Brunnermann</li>
        <li>Ravi Sandhu</li>
        <li>Tasha Okoro</li>
      </ul>
    </div>
  </section>
</div>
</body>
</html>
```